Website design (Wordpress theme) for SkyMerit, Education industry

We need a wordpress design for company website. We are based in the Netherlands and provide IT services to schools. We are currently developing a Learning Management System (LMS) that will be delivered as a Cloud service. This product will make it easier for both students and teachers to structure the process of learning. And will enable teachers to include more digital content into their lessons. We believe that in the future IT at schools should be simple and must always work.

We already have a logo and corresponding colors (blue and dark grey) that should be incorporated in the new website. They are attached to this brief.

The final design should communicate simplicity, flexibility and must have a fresh and modern look. When they look at our site our customers much see a company/product that is simple to do business with or simple to use. A company has professional products and is easy to do business with and maybe even fun to use (without being childish).

Target Market(s)

Education (schools). High school and primary level.

Industry/Entity Type

Industry

Requirements
Must have
• the design must consist of a landing (first) page and some pages for content. A good way to include video (YouTube). In the sidebar there should be a place for a twitter feed. Also, a part of the site will probably consist of a blog.
Nice to have
• If you look at our attached logo, you will see that the cloud has a little 'thingy' at the bottom. This can be used to display the cloud as a speech balloon. Maybe it is a nice and playful idea to include a figure that produces a speech balloon (which is part of our logo)

```html
<!DOCTYPE html>
<html lang="en">
<head>
<meta charset="utf-8">
<title>SkyMerit – Teach What You Love</title>
<link href="https://fonts.googleapis.com/css2?family=Fira+Sans:wght@400;500;600&family=Arimo:wght@400;700&display=swap" rel="stylesheet">
<style>
:root{
  --brand-blue:#1a9fd8;
  --brand-grey:#4a4a4a;
  --hero-blue:#0a6fb4;
  --hero-blue-deep:#075a98;
  --nav-darker:#2a2a2a;
  --text:#555;
  --heading-blue:#1670b5;
  --link-blue:#1b6fb8;
  --green:#5aa12a;
  --card-bg:#f1f1f1;
  --card-line:#dedede;
  --footer:#1f1f1f;
  --ribbon:#1b74c5;
}
*{box-sizing:border-box;margin:0;padding:0}
html,body{width:997px;height:1200px;overflow:hidden;background:#fff}
body{position:relative;font-family:"Arimo",Arial,sans-serif;color:var(--text)}
.abs{position:absolute}

/* Header */
.site-header{left:0;top:0;width:997px;height:116px;background:linear-gradient(#fdfdfd,#e8e8e8);border-bottom:3px solid #444}
.brand{left:10px;top:38px;display:flex;align-items:center;gap:12px}
.brand-dot{width:46px;height:46px;border-radius:50%;background:var(--brand-blue)}
.brand-name{font-family:"Fira Sans",sans-serif;font-weight:600;font-size:40px;color:var(--brand-grey);letter-spacing:-.5px}
.util-nav{left:735px;top:27px;width:252px;height:20px;background:linear-gradient(#d9d9d9,#b9b9b9);border-radius:10px 10px 0 0;display:flex;justify-content:space-around;align-items:center;font-size:10px;color:#555;padding:0 10px}
.main-nav{left:331px;top:47px;width:660px;height:39px;background:linear-gradient(#555,var(--nav-darker));border-radius:3px;display:flex;box-shadow:0 1px 2px rgba(0,0,0,.4)}
.main-nav a{flex:auto;text-align:center;line-height:39px;color:#fff;text-decoration:none;font-family:"Fira Sans",sans-serif;font-weight:500;font-size:17px;border-right:1px solid #222;box-shadow:inset -1px 0 0 #666}
.main-nav a:last-child{border:0;box-shadow:none}

/* Hero */
.hero-copy{left:0;top:117px;width:435px;height:328px;background:linear-gradient(135deg,var(--hero-blue-deep),var(--hero-blue) 60%,#1283c6)}
.hero-title{left:43px;top:160px;font-family:"Fira Sans",sans-serif;font-weight:500;font-size:36px;color:#fff;text-shadow:0 2px 3px rgba(0,0,0,.35)}
.hero-sub{left:44px;top:250px;font-family:"Fira Sans",sans-serif;font-size:26px;line-height:35px;color:#fff}
.hero-cta{left:91px;top:356px;width:260px;height:49px;border-radius:6px;background:linear-gradient(#f6f55a,#d8d20c);border:1px solid #a8a40a;box-shadow:0 2px 4px rgba(0,0,0,.35);font-weight:700;font-size:26px;color:#2e3b10;text-align:center;line-height:47px}
.hero-photo{left:435px;top:117px;width:562px;height:328px;background:linear-gradient(120deg,#e4e4e0 0%,#cfc7bd 35%,#9ab0c8 60%,#e9eaeb 100%)}

/* Feature cards */
.feature{top:460px;width:212px;height:119px;background:linear-gradient(#f7f7f7,#ececec);border:1px solid #e1e1e1;border-radius:6px;box-shadow:0 1px 3px rgba(0,0,0,.08)}
.feature h3{position:absolute;left:56px;top:14px;font-family:"Fira Sans",sans-serif;font-weight:500;font-size:16px;color:#555}
.feature p,.feature ul{position:absolute;left:56px;top:38px;width:140px;font-size:10px;line-height:16px;color:#666;list-style:none}
.feature ul{top:47px;left:58px}
.feature li{position:relative;padding-left:8px}
.feature li::before{content:"•";position:absolute;left:0;color:#888}
.feature svg{position:absolute;left:8px;top:22px}

/* How it works */
.how-title{left:42px;top:602px;width:571px;font-size:19px;font-weight:400;color:var(--heading-blue);border-bottom:1px solid #ccc;padding-bottom:2px}
.body-copy{font-size:10.9px;line-height:14.5px;color:#666;width:572px;left:42px}
.btn{top:719px;width:151px;height:43px;border-radius:4px;font-size:12px;display:flex;align-items:center;justify-content:center;gap:8px}
.btn-demo{left:42px;background:linear-gradient(#8fd35a,#5bb12b);border:1px solid #4c9a22;color:#2f5d12}
.btn-trial{left:213px;background:linear-gradient(#9fd0f0,#5fa6d9);border:1px solid #4b8fc5;color:#24507a}
.btn-buy{left:382px;background:linear-gradient(#fde89a,#f3c957);border:1px solid #d9ab36;color:#8a5a10}
.btn i{width:17px;height:17px;border:1.5px solid currentColor;border-radius:50%;display:inline-block}

/* Panels */
.panel{top:836px;height:241px;background:var(--card-bg);border:1px solid var(--card-line);border-radius:4px}
.ribbon{top:844px;height:33px;background:var(--ribbon);color:#fff;font-size:16px;line-height:33px;padding-left:27px;clip-path:polygon(0 0,100% 0,94% 100%,0 100%)}
.post-thumb{width:42px;height:42px;background:linear-gradient(#8aa6c4,#6a5a4c);border:2px solid #fff;box-shadow:0 0 0 1px #bbb}
.post-text{font-size:10.5px;line-height:14.5px;color:#444;width:215px}
.reply{width:46px;height:21px;background:var(--ribbon);color:#fff;font-size:11px;line-height:21px;text-align:center;border-radius:3px}
.meta{width:171px;height:21px;background:#555;color:#fff;font-size:11px;line-height:21px;text-align:center;border-radius:3px}
.quote{left:382px;width:205px;font-size:10.5px;line-height:14.5px;color:#444}
.rule{left:381px;width:215px;height:1px;background:#ddd}

/* Sidebar */
.sidebar{left:648px;top:601px;width:298px;height:343px;border:1px solid #ddd;border-radius:4px;background:#fff}
.side-block{left:668px;width:270px}
.side-block h4{font-family:"Fira Sans",sans-serif;font-weight:500;font-size:17px;color:var(--green);display:flex;align-items:center;gap:8px}
.side-block p{margin-top:12px;font-family:"Fira Sans",sans-serif;font-size:11.6px;line-height:16px;color:#444}
.side-block a{color:var(--link-blue);text-decoration:underline}
.side-rule{left:668px;width:266px;height:1px;background:#ddd}
.tweets{left:652px;top:958px;width:288px;height:114px;background:#fff;border:1px solid #ddd;box-shadow:0 1px 3px rgba(0,0,0,.15)}
.tweets-inner{position:absolute;left:6px;top:6px;right:6px;bottom:6px;background:#bfe5f3;border:1px solid #9fd0e4}
.tweets h5{position:absolute;left:10px;top:6px;font-family:Georgia,serif;font-weight:700;font-style:italic;font-size:14px;color:#333}
.tweet{position:absolute;left:10px;top:36px;width:256px;height:47px;background:#a9dcef;border-radius:5px;font-size:8.5px;line-height:12px;padding:6px 8px;color:#234}
.tweet a{color:#1b5f8a}
.tweets small{position:absolute;right:8px;bottom:8px;font-size:7.5px;color:#234}

/* Footer */
.site-footer{left:0;top:1122px;width:997px;height:78px;background:var(--footer)}
.social{position:absolute;top:25px;width:27px;height:27px;border-radius:4px}
.copyright{position:absolute;right:52px;top:28px;font-size:11px;color:#bbb}
</style>
</head>
<body>

<header class="site-header abs">
  <div class="brand abs"><span class="brand-dot"></span><span class="brand-name">SkyMerit</span></div>
  <nav class="util-nav abs"><span>About</span><span>Contact</span><span>Developer API</span><span>Login</span></nav>
  <nav class="main-nav abs">
    <a>Home</a><a>Pricing</a><a>Tour</a><a>Mobile</a><a>Our Customers</a><a>Support</a><a>Blog</a>
  </nav>
</header>

<section class="hero-copy abs"></section>
<h1 class="hero-title abs">Teach What You Love</h1>
<p class="hero-sub abs">The world’s most user-friendly<br>Learning Management System</p>
<div class="hero-cta abs">Create a Course</div>
<div class="hero-photo abs" role="img" aria-label="Photo of a family learning together at a laptop"></div>

<div class="feature abs" style="left:39px">
  <svg width="40" height="64" viewBox="0 0 40 64"><path d="M20 4a15 15 0 0 0-9 27c2 2 3 5 3 9h12c0-4 1-7 3-9A15 15 0 0 0 20 4z" fill="none" stroke="#1b74c5" stroke-width="3"/><rect x="14" y="44" width="12" height="6" rx="2" fill="#1b74c5"/></svg>
  <h3>Quick Start</h3>
  <ul style="width:135px"><li>Register FREE</li><li>Be LIVE in minutes</li><li>All your eLearning will be ready for deployment</li></ul>
</div>
<div class="feature abs" style="left:273px">
  <svg width="42" height="64" viewBox="0 0 42 64"><rect x="10" y="2" width="8" height="26" rx="4" fill="#1b74c5"/><path d="M6 26h30v14a12 12 0 0 1-12 12h-6A12 12 0 0 1 6 40z" fill="#1b74c5"/></svg>
  <h3>Test Drive</h3>
  <ul style="width:142px"><li>Demo SkyMerit ease of use</li><li>Upload existing learning materials, booklets, SCORM, Slide decks or Video</li></ul>
</div>
<div class="feature abs" style="left:505px">
  <svg width="40" height="64" viewBox="0 0 40 64"><text x="8" y="46" font-family="Arimo,sans-serif" font-size="48" fill="#1b74c5">$</text></svg>
  <h3>Sell Your Training</h3>
  <p style="width:136px">Make it available in our catalogue of training courses, your own Web Shop, and syndicate your training on the web.</p>
</div>
<div class="feature abs" style="left:736px">
  <svg width="42" height="64" viewBox="0 0 42 64"><path d="M4 10l26-6v50L4 60z" fill="#1b74c5"/><path d="M30 4l6 4v50l-6-4z" fill="#0e4f8f"/></svg>
  <h3>Need Training?</h3>
  <p style="width:150px">FREE Learning Platform! Purchase from SkyMerit Training Library, Brand your own LMS, Distribute courses to your Organization.</p>
</div>

<h2 class="how-title abs">How SkyMerit works</h2>
<p class="body-copy abs" style="top:635px">Lorem ipsum dolor sit amet, consectetur adipisicing elit, sed do eiusmod tempor incididunt ut labore et dolore magna aliqua. Ut enim ad minim veniam, quis nostrud exercitation ullamco laboris nisi ut aliquip ex ea commodo consequat.Lorem ipsum dolor sit amet, consectetur adipisicing elit, sed do eiusmod tempor incididunt ut labore et dolore magna aliqua. Ut enim ad minim veniam, quis nostrud exercitation ullamco laboris nisi ut aliquip ex ea commodo consequat.</p>
<div class="btn btn-demo abs">ONLINE DEMO <i></i></div>
<div class="btn btn-trial abs">GET FREE TRIAL <i></i></div>
<div class="btn btn-buy abs">PURCHASE NOW <i></i></div>
<p class="body-copy abs" style="top:777px">Lorem ipsum dolor sit amet, consectetur adipisicing elit, sed do eiusmod tempor incididunt ut labore et dolore magna aliqua. Ut enim ad minim veniam, quis nostrud exercitation ullamco laboris nisi ut aliquip ex ea commodo consequat.</p>

<section class="panel abs" style="left:41px;width:296px"></section>
<div class="ribbon abs" style="left:32px;width:178px">From the Blog</div>
<div class="post-thumb abs" style="left:58px;top:894px" role="img" aria-label="Author avatar"></div>
<p class="post-text abs" style="left:111px;top:891px">Lorem ipsum dolor sit amet, consectetur adipisicing elit, sed do eiusmod tempor incididunt ut labore et dolore magna aliqua.</p>
<div class="reply abs" style="left:56px;top:945px">Reply</div>
<div class="meta abs" style="left:113px;top:946px">5 Comments &nbsp;|&nbsp; posted on 12 July</div>
<div class="post-thumb abs" style="left:58px;top:986px" role="img" aria-label="Author avatar"></div>
<p class="post-text abs" style="left:111px;top:983px">Lorem ipsum dolor sit amet, consectetur adipisicing elit, sed do eiusmod tempor incididunt ut labore et dolore magna aliqua.</p>
<div class="reply abs" style="left:56px;top:1037px">Reply</div>
<div class="meta abs" style="left:113px;top:1038px">5 Comments &nbsp;|&nbsp; posted on 12 July</div>

<section class="panel abs" style="left:361px;width:266px"></section>
<div class="ribbon abs" style="left:352px;width:178px">Testimonials</div>
<p class="quote abs" style="top:893px">Lorem ipsum dolor sit amet, consectetur adipisicing elit, sed do eiusmod tempor incididunt ut labore et dolore ...</p>
<div class="rule abs" style="top:947px"></div>
<p class="quote abs" style="top:959px">Lorem ipsum dolor sit amet, consectetur adipisicing elit, sed do eiusmod tempor incididunt ut labore et dolore ...</p>
<div class="rule abs" style="top:1013px"></div>
<p class="quote abs" style="top:1024px">Lorem ipsum dolor sit amet, consectetur adipisicing elit, sed do eiusmod tempor incididunt ut labore et dolore ...</p>

<aside class="sidebar abs"></aside>
<div class="side-block abs" style="top:621px">
  <h4><svg width="18" height="18" viewBox="0 0 18 18"><path d="M1 3l5-2 6 2 5-2v14l-5 2-6-2-5 2z" fill="var(--green)"/></svg>Take the SkyMerit tour</h4>
  <p><a>A Learning Management System thats easy to use</a>! SkyMerit makes the management and delivery of web-based training courses easy.</p>
</div>
<div class="side-rule abs" style="top:720px"></div>
<div class="side-block abs" style="top:731px">
  <h4><svg width="14" height="20" viewBox="0 0 14 20"><rect x="1" y="1" width="12" height="18" rx="2" fill="none" stroke="var(--green)" stroke-width="2"/><rect x="5" y="15" width="4" height="2" fill="var(--green)"/></svg>Learning on the go</h4>
  <p><a>Get started with mobile learning</a>. Whether you’re ready or not the mobile learning revolution has begun!</p>
</div>
<div class="side-rule abs" style="top:829px"></div>
<div class="side-block abs" style="top:839px">
  <h4><svg width="22" height="18" viewBox="0 0 22 18"><rect x="1" y="1" width="20" height="13" fill="none" stroke="var(--green)" stroke-width="2"/><path d="M9 4l5 3.5-5 3.5z" fill="var(--green)"/><rect x="6" y="15" width="10" height="2" fill="var(--green)"/></svg>Watch a quick overview</h4>
  <p><a>There are heaps of great features</a>. Watch our short, but informative video outlining some our key features and benefits.</p>
</div>

<div class="tweets abs">
  <div class="tweets-inner">
    <h5>my recent tweets</h5>
    <div class="tweet"><b>Are you color blind? Put it to the test!</b> <a>http://sm.link/k4rT9q</a> (via @PixelHarbor) <a>about an hour ago</a></div>
    <small><b>» follow me: @LenaVoss</b></small>
  </div>
</div>

<footer class="site-footer abs">
  <span class="social" style="left:49px;background:#6cc4e6"></span>
  <span class="social" style="left:87px;background:#3b5b9c"></span>
  <span class="social" style="left:124px;background:#2a7ab0"></span>
  <span class="social" style="left:162px;background:#f0821e"></span>
  <span class="social" style="left:199px;background:#e9e9e9"></span>
  <span class="social" style="left:236px;background:#3f6fb4"></span>
  <span class="social" style="left:272px;background:#3aa845"></span>
  <p class="copyright">Copyright @ 2011 SkyMerit.com. All Rights Reserved.</p>
</footer>

</body>
</html>
```